Copper Ridge Athletics Web Design

Need to completely update website - simple and clean look - informative
this will be our main source for booking appointments etc. needs to have baseball and softball content. we currently have a site - looking to update - we would like you to design and add to our current site.

Target Market(s)

ages 15-45, youth and parents for kids- softball and baseball players /fitness

Industry/Entity Type

baseball and softball indoor training facility

Coding

Coded - Design and coding required

Number of Pages Required

5+ page

Colors

Designer to choose colors to be used in the design.

Requirements
Must have
• our colors of business are green and black- we need you to completely set up the website for us
Nice to have
• out current webiste is www.copperridge482.example

```html
<!DOCTYPE html>
<html lang="en">
<head>
<meta charset="utf-8">
<title>Copper Ridge Athletics</title>
<link href="https://fonts.googleapis.com/css2?family=Roboto:wght@400;500;700;900&display=swap" rel="stylesheet">
<style>
:root{
  --green:#3df21f;
  --green-deep:#2fc816;
  --black:#000;
  --ink:#0b0b0b;
  --charcoal:#1a1a1a;
  --slate:#3a3a3a;
  --white:#fff;
  --muted:#bdbdbd;
}
*{box-sizing:border-box;margin:0;padding:0}
html,body{width:1200px;height:2812px;overflow:hidden;background:var(--black);font-family:"Roboto",sans-serif;color:var(--white)}
.page{position:relative;width:1200px;height:2812px}

.site-header{position:absolute;top:0;left:0;width:1200px;height:100px;background:var(--black);display:flex;align-items:center;padding:0 48px}
.brand{display:flex;align-items:center;gap:14px}
.brand-dot{width:34px;height:34px;border-radius:50%;background:var(--green)}
.brand-name{font-weight:900;font-size:24px;letter-spacing:1px;text-transform:uppercase;color:var(--white)}
.main-nav{margin-left:auto;display:flex;gap:22px;font-size:15px;font-weight:700;text-transform:uppercase}
.main-nav a{color:var(--white);text-decoration:none}
.main-nav a.active{color:var(--green)}
.btn-login{margin-left:62px;background:var(--green);color:var(--black);font-weight:700;font-size:15px;padding:10px 30px;border-radius:4px;text-transform:uppercase}

.hero{position:absolute;top:100px;left:0;width:1200px;height:572px;background:linear-gradient(100deg,#1d2428 0%,#3e4850 40%,#5e666a 60%,#2c3a30 100%)}
.hero-shade{position:absolute;inset:0;background:linear-gradient(90deg,rgba(0,0,0,.55),rgba(0,0,0,0) 55%)}
.hero-copy{position:absolute;left:136px;top:160px}
.eyebrow{font-size:15px;font-weight:700;letter-spacing:3px;text-transform:uppercase}
.hero-title{font-size:60px;font-weight:900;color:var(--green);text-transform:uppercase;line-height:1.05;margin-top:6px}
.hero-sub{font-size:17px;font-weight:700;text-transform:uppercase;margin-top:8px}
.hero-actions{display:flex;gap:22px;margin-top:40px}
.btn{font-size:16px;font-weight:700;text-transform:uppercase;padding:14px 20px;border-radius:3px}
.btn-primary{background:var(--green);color:var(--black)}
.btn-outline{border:2px solid var(--white);color:var(--white)}
.hero-arrow{position:absolute;top:250px}
.hero-arrow.left{left:44px}.hero-arrow.right{right:44px}

.feature-row{position:absolute;top:672px;left:0;width:1200px;height:400px;display:flex}
.feature-photo{width:400px;height:400px}
.photo-balls{background:linear-gradient(135deg,#e8e4dc,#8a7f74 50%,#2d2a28)}
.photo-cage{background:linear-gradient(160deg,#1a1f22,#4b5a4a 55%,#7e9c6c)}
.contact-card{width:400px;height:400px;background:var(--green);color:var(--black);display:flex;flex-direction:column;align-items:center;padding-top:72px;font-weight:700}
.contact-card .addr{font-size:19px;text-align:center;line-height:1.9;margin-top:36px}
.contact-card .phone{display:flex;align-items:center;gap:26px;font-size:24px;margin-top:42px}

.motto{position:absolute;top:1072px;left:0;width:1200px;height:268px;background:linear-gradient(90deg,#3b3b3b,#565656 50%,#3b3b3b);text-align:center;padding-top:90px}
.motto h2{font-size:50px;font-weight:900;text-transform:uppercase}
.motto h2 span{color:var(--green)}
.motto p{font-size:24px;margin-top:8px}

.hours{position:absolute;top:1340px;left:0;width:1200px;height:480px;background:var(--black)}
.hours-photo{position:absolute;left:128px;top:118px;width:492px;height:262px;background:linear-gradient(180deg,#2a2a2a,#4a4a4a 60%,#1b1b1b);box-shadow:inset 0 0 0 3px rgba(61,242,31,.25)}
.hours-copy{position:absolute;left:660px;top:150px}
.hours-copy h2{font-size:48px;font-weight:900;text-transform:uppercase;line-height:1;margin-top:8px}
.hours-copy h2 span{color:var(--green)}
.hours-copy h3{font-size:20px;font-weight:400;text-transform:uppercase;margin-top:6px}
.divider{width:360px;height:1px;background:#555;margin:22px 0 20px}
.hours-list{list-style:none;font-size:14px;line-height:2.35;color:var(--muted)}

.mailing{position:absolute;top:1820px;left:0;width:1200px;height:440px;background:var(--slate);padding:144px 0 0 128px}
.mailing h2{font-size:52px;font-weight:900;text-transform:uppercase;line-height:1}
.mailing h2 span{color:var(--green)}
.mailing h3{font-size:22px;font-weight:400;text-transform:uppercase;margin-top:14px}
.signup{display:flex;gap:30px;margin-top:32px;align-items:center}
.field{height:42px;background:#222;border-bottom:2px solid #777;padding:0 14px;font-size:18px;display:flex;align-items:center;text-transform:uppercase}
.field.name{width:240px}.field.email{width:370px}
.btn-join{background:var(--green);color:var(--black);font-weight:700;font-size:18px;padding:10px 34px}
.note{font-size:11px;color:#ccc;margin-top:22px}

.site-footer{position:absolute;top:2260px;left:0;width:1200px;height:460px;background:linear-gradient(135deg,#141414,#262626 50%,#1c1c1c)}
.footer-panel{position:absolute;left:0;top:0;width:520px;height:460px}
.footer-info{position:absolute;left:90px;top:100px}
.footer-mark{width:130px;height:130px;border-radius:50%;background:var(--white)}
.footer-name{font-size:17px;font-weight:900;text-transform:uppercase;margin-top:18px}
.footer-addr{font-size:16px;font-weight:700;line-height:1.5;margin-top:8px}
.socials{display:flex;gap:18px;margin-top:22px}
.socials span{width:26px;height:26px;border-radius:50%;background:var(--white)}

.bottom-bar{position:absolute;top:2720px;left:0;width:1200px;height:92px;background:var(--black);display:flex;align-items:center;justify-content:center;gap:22px;font-size:14px;font-weight:700;text-transform:uppercase}
.btn-staff{margin-left:40px;border:1px solid var(--white);padding:10px 20px;font-size:13px}
</style>
</head>
<body>
<div class="page">

  <header class="site-header">
    <div class="brand"><span class="brand-dot"></span><span class="brand-name">Copper Ridge Athletics</span></div>
    <nav class="main-nav">
      <a class="active">Home</a><a>About</a><a>Facilities</a><a>Lessons</a><a>Team Rental Pricing</a><a>Careers</a><a>Classes | Camps</a>
    </nav>
    <span class="btn-login">Login</span>
  </header>

  <section class="hero" role="img" aria-label="Baseball pitcher mid-delivery on an indoor field">
    <div class="hero-shade"></div>
    <svg class="hero-arrow left" width="28" height="56" viewBox="0 0 28 56"><path d="M24 4 4 28l20 24" fill="none" stroke="#fff" stroke-width="3"/></svg>
    <svg class="hero-arrow right" width="28" height="56" viewBox="0 0 28 56"><path d="M4 4l20 24L4 52" fill="none" stroke="#fff" stroke-width="3"/></svg>
    <div class="hero-copy">
      <p class="eyebrow">Baseball Training</p>
      <h1 class="hero-title">Creating Pros</h1>
      <p class="hero-sub">In baseball and softball trainings</p>
      <div class="hero-actions">
        <span class="btn btn-primary">Book Appointment</span>
        <span class="btn btn-outline">Contact Us</span>
      </div>
    </div>
  </section>

  <section class="feature-row">
    <div class="feature-photo photo-balls" role="img" aria-label="Row of baseballs close up"></div>
    <div class="feature-photo photo-cage" role="img" aria-label="Indoor batting cage with netting and turf"></div>
    <div class="contact-card">
      <svg width="40" height="58" viewBox="0 0 40 58"><path d="M20 0C9 0 0 9 0 20c0 15 20 38 20 38s20-23 20-38C40 9 31 0 20 0z" fill="#000"/><circle cx="20" cy="20" r="7" fill="#3df21f"/></svg>
      <p class="addr">2480 Alder Creek Rd Suite #100<br>MAPLE GROVE, CA 95210</p>
      <p class="phone">
        <svg width="26" height="26" viewBox="0 0 24 24"><path d="M6.6 10.8a15 15 0 0 0 6.6 6.6l2.2-2.2c.3-.3.7-.4 1-.2 1.1.4 2.3.6 3.6.6.6 0 1 .4 1 1V20c0 .6-.4 1-1 1A17 17 0 0 1 3 4c0-.6.4-1 1-1h3.5c.6 0 1 .4 1 1 0 1.3.2 2.5.6 3.6.1.3 0 .7-.2 1z" fill="#000"/></svg>
        555-014-7183
      </p>
    </div>
  </section>

  <section class="motto" role="img" aria-label="Faint baseball photo backdrop">
    <h2>Be the <span>Best</span> at it</h2>
    <p>Ultimate baseball training's best programs</p>
  </section>

  <section class="hours">
    <div class="hours-photo" role="img" aria-label="Facility lounge with seating and green lit walls"></div>
    <div class="hours-copy">
      <p class="eyebrow" style="font-size:13px">When to come visit</p>
      <h2><span>Ready</span> to serve</h2>
      <h3>Our operating hours</h3>
      <div class="divider"></div>
      <ul class="hours-list">
        <li>MON-THUR : 3:00-9:00 pm</li>
        <li>FRI : 4:00 pm - 7:00 pm</li>
        <li>SAT: Closed</li>
        <li>SUN: Closed</li>
      </ul>
    </div>
  </section>

  <section class="mailing">
    <h2>Join our <span>Mailing</span> list</h2>
    <h3>To receive our latest updates</h3>
    <div class="signup">
      <span class="field name">Name</span>
      <span class="field email">Email</span>
      <span class="btn-join">JOIN</span>
    </div>
    <p class="note">We promise not to spam you!</p>
  </section>

  <footer class="site-footer" role="img" aria-label="Street map around the facility">
    <svg class="footer-panel" viewBox="0 0 520 460" width="520" height="460"><polygon points="0,0 350,0 520,460 0,460" fill="#2fc816" opacity=".85"/></svg>
    <div class="footer-info">
      <div class="footer-mark"></div>
      <p class="footer-name">Copper Ridge Athletics</p>
      <p class="footer-addr">2480 Alder Creek Rd Suite #100<br>MAPLE GROVE, CA 95210</p>
      <div class="socials"><span></span><span></span><span></span></div>
    </div>
  </footer>

  <nav class="bottom-bar">
    <span>Home</span><span>About</span><span>Facilities</span><span>Lessons</span><span>Team Rental Pricing</span><span>Careers</span><span>Classes | Camps</span>
    <span class="btn-staff">Staff Login</span>
  </nav>

</div>
</body>
</html>
```